Simple : A Therapist is looking for a Design

Im lookind for a business card design for my new business .
my therapy field - Attuned Somatic Release .
Its part of Osteopatic medicine .
its gental, not invasive method that focus on the bones of the skull (cranial) .
i want some kind of skull in it like the attached photo.

Target Market(s)

people that suffer from pain

Industry/Entity Type

Physical Therapy

Contact Information for Business Card

i want people to understand this is diffrent kind of therapy
its anatomy base , gental and give outstanding result .

Font styles to use
Serif

Colors
fee18a
cadf82
fbc994
cedeed
fbe7d2
fff3d1

Requirements
Must have
• one side: my name (Eliran Tsabari) ,
• phone number ( 0541762908)
• email (tsabarieliran@mailvent.net)
• other side : Attuned Somatic Release
Nice to have
• i want some kind of skull in it like the attached photo.
• very powrful, accurate and smart.
• nice colores (maybe lite orange?, lite green?) , simple, relax, smart

```html
<!DOCTYPE html>
<html lang="en">
<head>
<meta charset="utf-8">
<title>Eliran Tsabari — Business Card</title>
<link rel="stylesheet" href="https://fonts.googleapis.com/css2?family=Tinos&display=swap">
<style>
  :root {
    --backdrop: #ece8e1;
    --card: #ffffff;
    --slate-blue: #8ea3b7;
    --soft-yellow: #eccf78;
    --ink-grey: #8b8b8b;
    --mark-blue: #cedeed;
    --shadow: rgba(40, 30, 15, 0.35);
  }
  * { margin: 0; padding: 0; box-sizing: border-box; }
  html, body {
    width: 900px;
    height: 1200px;
    overflow: hidden;
    background: var(--backdrop);
  }
  .canvas {
    position: relative;
    width: 900px;
    height: 1200px;
    font-family: "Tinos", "Times New Roman", serif;
  }
  .card {
    position: absolute;
    left: 86px;
    width: 732px;
    height: 428px;
    background: var(--card);
    border-radius: 28px;
    box-shadow: 4px 6px 10px var(--shadow);
  }
  .card--front { top: 135px; }
  .card--back { top: 645px; }

  .contact-block {
    position: absolute;
    top: 158px;
    left: 0;
    width: 100%;
    text-align: center;
    padding-left: 6px;
  }
  .contact-block__name {
    font-size: 29px;
    letter-spacing: 4px;
    color: var(--slate-blue);
    line-height: 30px;
  }
  .contact-block__role {
    font-size: 17px;
    letter-spacing: 2.5px;
    color: var(--soft-yellow);
    line-height: 22px;
    margin-bottom: 8px;
  }
  .contact-block__line {
    font-size: 16px;
    letter-spacing: 2px;
    color: var(--ink-grey);
    line-height: 23px;
  }

  .brand {
    position: absolute;
    top: 150px;
    left: 122px;
    display: flex;
    align-items: center;
    gap: 22px;
  }
  .brand__mark {
    width: 128px;
    height: 128px;
    display: block;
  }
  .brand__name {
    font-size: 21px;
    color: var(--ink-grey);
    letter-spacing: 0.3px;
    text-transform: uppercase;
    white-space: nowrap;
  }
</style>
</head>
<body>
  <main class="canvas">
    <section class="card card--front" aria-label="Card front">
      <div class="contact-block">
        <p class="contact-block__name">ELIRAN TSABARI</p>
        <p class="contact-block__role">THERAPIST</p>
        <p class="contact-block__line">054-176-2908</p>
        <p class="contact-block__line">tsabarieliran@mailvent.net</p>
      </div>
    </section>

    <section class="card card--back" aria-label="Card back">
      <div class="brand">
        <svg class="brand__mark" viewBox="0 0 128 128" aria-hidden="true">
          <circle cx="64" cy="64" r="64" fill="var(--mark-blue)"/>
        </svg>
        <p class="brand__name">Attuned Somatic Release</p>
      </div>
    </section>
  </main>
</body>
</html>
```